Brintell's Business Card

I need some designs for a new business card including the new logo attached. An old example of our business card is also attached to show all the data that should be included on the new design.
**I added some more examples someone had mocked up**

Contact Information for Business Card

Should include all info on other examples uploaded.

```html
<!DOCTYPE html>
<html lang="en">
<head>
<meta charset="utf-8">
<title>Brintell's Business Card</title>
<link href="https://fonts.googleapis.com/css2?family=Montserrat:wght@400;500;600;700&display=swap" rel="stylesheet">
<style>
  :root {
    --brand-blue: #1a6fbc;
    --brand-red: #e3232b;
    --ink: #2b2b2b;
    --paper: #ffffff;
    --backdrop: #d8d1c4;
  }
  * { margin: 0; padding: 0; box-sizing: border-box; }
  html, body { width: 900px; height: 1200px; overflow: hidden; }
  body {
    background: var(--backdrop);
    font-family: 'Montserrat', sans-serif;
    position: relative;
  }
  .card {
    position: absolute;
    left: 80px;
    width: 742px;
    height: 440px;
    border-radius: 30px;
    overflow: hidden;
    box-shadow: 0 6px 14px rgba(0,0,0,0.35);
  }
  .card-front { top: 132px; background: var(--paper); }
  .card-back { top: 638px; background: var(--brand-blue); }

  /* front */
  .front-brand {
    position: absolute;
    left: 60px; width: 300px; top: 150px;
    text-align: center;
  }
  .brand-mark {
    display: block;
    margin: 0 auto 22px;
    width: 60px; height: 60px;
    border-radius: 50%;
    background: var(--brand-red);
  }
  .brand-name {
    font-weight: 700;
    font-size: 44px;
    line-height: 1;
    color: var(--brand-blue);
    letter-spacing: 0.5px;
  }
  .brand-descriptor {
    margin-top: 6px;
    font-weight: 600;
    font-size: 12.5px;
    color: var(--brand-red);
  }
  .divider {
    position: absolute;
    left: 388px; top: 133px;
    width: 2px; height: 152px;
    background: var(--brand-blue);
  }
  .contact {
    position: absolute;
    left: 423px; top: 128px;
    color: var(--ink);
  }
  .contact-name {
    font-weight: 700;
    font-size: 26px;
    color: var(--brand-blue);
    margin-bottom: 18px;
  }
  .service-area { font-size: 16px; line-height: 20px; margin-bottom: 22px; }
  .contact-line {
    display: flex; align-items: center; gap: 10px;
    font-size: 16px; line-height: 24px;
  }
  .contact-line svg { width: 16px; height: 16px; flex: none; }
  .front-bands {
    position: absolute; left: 0; bottom: 0;
    width: 742px; height: 42px;
  }
  .band-label {
    position: absolute; bottom: 0; height: 42px;
    display: flex; align-items: center; justify-content: center;
    color: #fff; font-weight: 500; font-size: 16px;
  }
  .band-family { left: 0; width: 380px; }
  .band-licensed { left: 390px; width: 352px; }

  /* back */
  .back-brand {
    position: absolute;
    left: 80px; top: 160px;
    display: flex; align-items: center; gap: 26px;
  }
  .back-brand .brand-mark { margin: 0; width: 100px; height: 100px; }
  .back-brand .brand-name { font-size: 64px; color: #fff; }
  .back-brand .brand-descriptor { font-size: 17px; margin-top: 4px; }
  .back-cta {
    position: absolute; left: 0; right: 0; top: 384px;
    text-align: center;
    color: #fff; font-weight: 500; font-size: 16px;
  }
</style>
</head>
<body>
  <section class="card card-front">
    <div class="front-brand">
      <span class="brand-mark"></span>
      <div class="brand-name">BRINTELL'S</div>
      <div class="brand-descriptor">AIR CONDITIONING &amp; HEATING SERVICE</div>
    </div>
    <div class="divider"></div>
    <div class="contact">
      <div class="contact-name">Mark Brintell</div>
      <div class="service-area">Serves Oakridge<br>IA &amp; Surrounding Areas</div>
      <div class="contact-line">
        <svg viewBox="0 0 16 16" aria-hidden="true"><path d="M1 6c0-2 3-3 7-3s7 1 7 3v1h-3V5.5H4V7H1z" fill="#e3232b"/><rect x="3" y="8" width="10" height="6" rx="1" fill="#e3232b"/><circle cx="8" cy="11" r="1.6" fill="#fff"/></svg>
        <span>555.014.2290</span>
      </div>
      <div class="contact-line">
        <svg viewBox="0 0 16 16" aria-hidden="true"><rect x="1" y="3.5" width="14" height="9" rx="1" fill="#1a6fbc"/><path d="M1.5 4l6.5 5 6.5-5" fill="none" stroke="#fff" stroke-width="1.3"/></svg>
        <span>hvacbrintell@mailbox.net</span>
      </div>
    </div>
    <svg class="front-bands" viewBox="0 0 742 42" aria-hidden="true">
      <polygon points="0,0 396,0 372,42 0,42" fill="#1a6fbc"/>
      <polygon points="406,0 742,0 742,42 380,42" fill="#e3232b"/>
    </svg>
    <div class="band-label band-family">FAMILY OWNED &amp; OPERATED</div>
    <div class="band-label band-licensed">LICENSED &amp; INSURED</div>
  </section>

  <section class="card card-back">
    <div class="back-brand">
      <span class="brand-mark"></span>
      <div>
        <div class="brand-name">BRINTELL'S</div>
        <div class="brand-descriptor">AIR CONDITIONING &amp; HEATING SERVICE</div>
      </div>
    </div>
    <div class="back-cta">CALL TODAY FOR ALL YOUR HVAC, REFRIGERATION &amp; PLUMBING NEEDS</div>
  </section>
</body>
</html>
```